We need help creating industry specific one page marketing flyers

We are kicking off a campaign to target specific industry verticals and need help creating / designing one pager marketing collateral for each industry.

See attached our first industry, healthcare. I created this but want to make it more professional looking.

Here is our website (the website is old, we're refreshing this in the near future). www.brookvane.com

I want it in powerpoint format so that I can make adjustments to the one pager and create PDFs from it as well.

Target Market(s)

Property managers and facilities managers

Industry/Entity Type

Industry

Requirements
Must have
• Tie to our corporate logo colors
• Use plant pictures and visuals to tell the story
• Must be in an editable format (e.g. powerpoint) so I can make tweaks to the content

```html
<!DOCTYPE html>
<html lang="en">
<head>
<meta charset="UTF-8">
<title>Brookvane – Indoor Plant Services for Healthcare Facilities</title>
<link href="https://fonts.googleapis.com/css2?family=Gelasio:wght@400&family=Questrial&display=swap" rel="stylesheet">
<style>
  :root{
    --leaf-green:#6fa23c;
    --band-green:#72a43f;
    --ink:#222222;
    --paper:#ffffff;
    --slate:#6d6d70;
    --backdrop:#e9e6e1;
    --photo-atrium-a:#5f7d3a;
    --photo-atrium-b:#c9c7bd;
    --photo-terrace-a:#bcbcb2;
    --photo-terrace-b:#7f9a4a;
    --photo-lobby-a:#d9d6d0;
    --photo-lobby-b:#4f7a36;
  }
  *{margin:0;padding:0;box-sizing:border-box;}
  html,body{width:960px;height:1200px;overflow:hidden;background:var(--backdrop);}
  .flyer{
    position:absolute;left:30px;top:18px;width:900px;height:1164px;
    background:var(--paper);overflow:hidden;
    font-family:"Questrial",sans-serif;color:var(--ink);
  }
  .brand-name{
    position:absolute;left:36px;top:86px;
    font-family:"Gelasio",serif;font-weight:400;font-size:74px;line-height:1;
    color:var(--leaf-green);letter-spacing:-0.5px;
  }
  .tagline{
    position:absolute;left:532px;top:66px;width:360px;
    font-family:"Gelasio",serif;font-weight:400;font-size:28px;line-height:34px;color:var(--leaf-green);
  }
  .photo{position:absolute;}
  .photo-atrium{left:0;top:219px;width:453px;height:338px;
    background:linear-gradient(100deg,var(--photo-atrium-a) 0%,#7e9a4c 35%,var(--photo-atrium-b) 70%,#e5e2d6 100%);}
  .photo-terrace{left:459px;top:219px;width:335px;height:248px;
    background:linear-gradient(160deg,var(--photo-terrace-a) 0%,#d8d5c9 45%,var(--photo-terrace-b) 100%);}
  .photo-lobby{left:458px;top:474px;width:442px;height:215px;
    background:linear-gradient(180deg,var(--photo-lobby-a) 0%,var(--photo-lobby-b) 45%,#5c8a3f 70%,#e2e0dc 100%);}
  .accent-block{position:absolute;left:801px;top:219px;width:99px;height:248px;background:var(--slate);}
  .welcome-band{
    position:absolute;left:0;top:562px;width:453px;height:127px;background:var(--band-green);
    padding:36px 0 0 19px;
    font-family:"Gelasio",serif;font-size:27px;line-height:35px;color:var(--paper);
  }
  .section-title{
    position:absolute;top:732px;
    font-family:"Gelasio",serif;font-weight:400;font-size:29px;line-height:34px;color:var(--leaf-green);
  }
  .title-expertise{left:22px;}
  .title-benefits{left:476px;}
  .body-copy{position:absolute;left:27px;width:392px;font-size:15px;line-height:23px;}
  .copy-clients{top:782px;}
  .copy-know-how{top:850px;}
  .consult{
    position:absolute;left:32px;top:950px;width:420px;
    font-family:"Gelasio",serif;font-size:22px;line-height:29.5px;
  }
  .consult .hl{color:var(--leaf-green);}
  .benefits{position:absolute;left:477px;top:779px;width:385px;list-style:none;}
  .benefits li{position:relative;padding-left:27px;font-size:15px;line-height:26px;}
  .benefits li + li{margin-top:16px;}
  .benefits li.gap-lg{margin-top:25px;}
  .benefits svg{position:absolute;left:0;top:5px;width:19px;height:15px;}
  .footer-bar{
    position:absolute;left:23px;top:1088px;width:846px;height:42px;border-radius:12px;
    background:var(--band-green);color:var(--paper);
    display:flex;align-items:center;justify-content:center;gap:28px;
    font-family:"Gelasio",serif;font-size:16.5px;
  }
</style>
</head>
<body>
  <main class="flyer">
    <div class="brand-name">Brookvane</div>
    <h1 class="tagline">Indoor Plant Design and Maintenance Services for Healthcare Facilities</h1>

    <div class="photo photo-atrium" role="img" aria-label="Hospital atrium lounge with a living green wall, yellow sofas and potted trees"></div>
    <div class="photo photo-terrace" role="img" aria-label="Glass-roofed corridor lined with large planters of bamboo and tropical plants"></div>
    <div class="accent-block"></div>
    <div class="photo photo-lobby" role="img" aria-label="Lobby with a flowering living plant wall and black lounge chairs"></div>

    <div class="welcome-band">We can help you make your<br>healthcare facility more welcoming!</div>

    <h2 class="section-title title-expertise">We know healthcare facilities</h2>
    <p class="body-copy copy-clients">We currently serve over 20 of the largest hospitals<br>and healthcare facilities across the Bay Area</p>
    <p class="body-copy copy-know-how">We understand what works in a hospital from<br>using the right moss to minimize dusty to the right<br>plant</p>
    <p class="consult">For a design consultation, please<br>contact <span class="hl">510-555-0148</span> or Dana Whitlock<br>at <span class="hl">whitlock@brookvane.com</span></p>

    <h2 class="section-title title-benefits">Benefits of plants...</h2>
    <ul class="benefits">
      <li><svg viewBox="0 0 20 16"><path d="M2 8 L8 13 L18 2" fill="none" stroke="#6fa23c" stroke-width="3" stroke-linecap="round" stroke-linejoin="round"/></svg>High impact amenity at a low cost</li>
      <li><svg viewBox="0 0 20 16"><path d="M2 8 L8 13 L18 2" fill="none" stroke="#6fa23c" stroke-width="3" stroke-linecap="round" stroke-linejoin="round"/></svg>Create a calming environment for patients</li>
      <li><svg viewBox="0 0 20 16"><path d="M2 8 L8 13 L18 2" fill="none" stroke="#6fa23c" stroke-width="3" stroke-linecap="round" stroke-linejoin="round"/></svg>Patients’ stress levels increase in the hospital,<br>however exposure to natural settings has the<br>ability to reduce stress and enhance the<br>process of healing</li>
      <li class="gap-lg"><svg viewBox="0 0 20 16"><path d="M2 8 L8 13 L18 2" fill="none" stroke="#6fa23c" stroke-width="3" stroke-linecap="round" stroke-linejoin="round"/></svg>Are proven to provide health benefits such as<br>cleaning indoor air</li>
    </ul>

    <footer class="footer-bar">
      <span>Brookvane, Inc. PO Box 41207 Alameda, CA 94501</span><span>|</span>
      <span>info@brookvane.com</span><span>|</span>
      <span>www.brookvane.com</span>
    </footer>
  </main>
</body>
</html>
```